Keen Volt Electrical in need of a business card design

We need a new business card designed for our electrical business. We have a logo already which I will attach below.
Would like the business card to be..
-BLACK background preferably, possibly white back ground behind logo if colours clash.
-White & Blue (logo blue) text
Something that makes the logo pop, & a modern look. Possibly minimal clean format.

REQUIRE:
-Logo on front & back

TEXT TO INCLUDE (ON ONE SIDE):

Tom Harlow
Director/Electrician
M: 0412 563 718
E:info@keenvoltelectrical.com.au
W:www.keenvoltelectrical.com.au
R.E.C 58431

Custom/New Homes
Renovations
Commercial Office/Shop Fit-outs
Communications & Security Cameras
Electric Vehicle Chargers
Airconditioning
Updates

Requirements
Nice to have
• Possibly even lighten the grey shades for the words 'Keen' & 'Volt' to be more easily read on a black background.

```html
<!DOCTYPE html>
<html lang="en">
<head>
<meta charset="utf-8">
<title>Keen Volt Electrical – Business Card</title>
<link rel="stylesheet" href="https://fonts.googleapis.com/css2?family=Montserrat:wght@300;400;500;700&display=swap">
<style>
  :root {
    --backdrop: #e8e8e8;
    --card-black: #050506;
    --card-edge: #111214;
    --brand-blue: #19a9e1;
    --text-white: #e6e6e6;
    --text-grey: #b9b9b9;
  }
  * { margin: 0; padding: 0; box-sizing: border-box; }
  html, body {
    width: 1200px;
    height: 1145px;
    overflow: hidden;
    background: var(--backdrop);
    font-family: "Montserrat", sans-serif;
  }
  .card {
    position: absolute;
    left: 250px;
    width: 700px;
    height: 444px;
    background: linear-gradient(135deg, var(--card-edge) 0%, var(--card-black) 55%);
    box-shadow: 0 14px 30px rgba(0,0,0,0.22);
    overflow: hidden;
  }
  .card--services { top: 95px; }
  .card--contact { top: 606px; }

  /* Brand name lockup */
  .brand {
    position: absolute;
    display: flex;
    align-items: center;
    gap: 10px;
  }
  .brand__square {
    width: 14px;
    height: 14px;
    background: var(--brand-blue);
  }
  .brand__name {
    font-weight: 500;
    font-size: 20px;
    color: var(--brand-blue);
    letter-spacing: 0.2px;
    white-space: nowrap;
  }
  .card--services .brand { left: 430px; top: 206px; }
  .card--contact .brand { left: 430px; top: 96px; }

  /* Services side */
  .services__accent {
    position: absolute;
    left: 0;
    top: 145px;
    width: 11px;
    height: 151px;
    background: var(--brand-blue);
  }
  .services__list {
    position: absolute;
    left: 42px;
    top: 136px;
    list-style: none;
    font-weight: 300;
    font-size: 19px;
    line-height: 27.6px;
    color: var(--text-grey);
  }

  /* Contact side */
  .contact {
    position: absolute;
    left: 56px;
    top: 168px;
  }
  .contact__name {
    font-weight: 700;
    font-size: 30px;
    color: var(--brand-blue);
    line-height: 1.1;
  }
  .contact__role {
    margin-top: 4px;
    font-weight: 400;
    font-size: 15px;
    color: var(--text-grey);
  }
  .contact__details {
    margin-top: 22px;
    list-style: none;
    font-weight: 400;
    font-size: 16px;
    line-height: 26px;
    color: var(--text-white);
  }
</style>
</head>
<body>

  <section class="card card--services" aria-label="Business card, services side">
    <div class="services__accent"></div>
    <ul class="services__list">
      <li>Custom/New Homes</li>
      <li>Renovations</li>
      <li>Commercial Office/Shop Fit-outs</li>
      <li>Communications &amp; Security Cameras</li>
      <li>Electric Vehicle Chargers</li>
      <li>Airconditioning</li>
    </ul>
    <div class="brand">
      <span class="brand__square"></span>
      <span class="brand__name">Keen Volt Electrical</span>
    </div>
  </section>

  <section class="card card--contact" aria-label="Business card, contact side">
    <div class="brand">
      <span class="brand__square"></span>
      <span class="brand__name">Keen Volt Electrical</span>
    </div>
    <div class="contact">
      <h1 class="contact__name">Tom Harlow</h1>
      <p class="contact__role">Director/Electrician</p>
      <ul class="contact__details">
        <li>0412 563 718</li>
        <li>info@keenvoltelectrical.com.au</li>
        <li>www.keenvoltelectrical.com.au</li>
      </ul>
    </div>
  </section>

</body>
</html>
```